International Student Travel Company needs a web page re-designed

Pellham Journeys is a worldwide leader in student educational and performing arts travel programs. We provide high-quality tours that exceed the expectations of our participants/customers and enhance a student's learning experiences. Our mission is to forever change how every student sees the world around them. Our company has 3 distinct brands: Pellham Journeys (www.pellhamjourneys.example), Brightwell Voyages (www.brightwellvoyages.example) and Northfield Heritage Trips & Band Jamborees (www.nfheri.example).

As part of our travel programs, we offer participants the option to purchase travel insurance. We are looking to re-design the page that offers each participant the option to buy insurance during their online registration process to maximize the number of customers who purchase the recommended option. The registration process is set up behind a password protected registration website.

Here is a link to view the current page for each brand:
https://accounts.pellhamjourneys.example/tech/demo/3172
https://accounts.brightwellvoyages.example/tech/demo/3172
https://accounts.nfheri.example/tech/demo/3172

We are attaching the HTML for the current page so you can start with the current format that this design is a part of- for example, the header & footer and the "Registration Step # section".

Please note that this current design was created for the "Brightwell Voyages" brand as you may note the use of the orange color on the page. We would like to design the page so that we can easily implement the same design for all 3 brands. As you will see from looking at the brands online, they all share a similar blue that can be used where we need a color as you will see on our SAMPLE mock-up that we have included as an attachment.

In our SAMPLE mock-up (file attached named "SAMPLE webpage mock-up.pdf") we have icons at the top of the insurance option which is meant to be a link to a PDF that is an advertisement for each type of travel insurance. So, however you decide to design that element, please make sure to include that as a link that will open a PDF in a new tab. The "None" option will open up the PDF attached named "Note to Parents.pdf". The "Student Deluxe" option will open up the PDF attached named "Marlow & Pike.pdf". The "Student Deluxe with CFAR" option will open up the PDF attached named "CFAR.pdf".

The sample mock-up is just a sample draft idea of how we would want it to look. Please feel free to re-design completely or as close to this design as you wish using your best design judgment. The goal is to make it look very professional and convince customers to select the recommended "Student Deluxe with CFAR" option as this will fully protect them in case they need to cancel.

It is very important to use all the copy as its presented since the language has all been approved by the insurance company's compliance team.

*VERY IMPORTANT*
Please design this so that it is MOBILE friendly. Many of our customers register for our trips on their mobile devices. So, because we are presenting 3 options to compare we need to make sure the design works well on small mobile screens. So, please present your designs for both large computer screens and small mobile devices so we can see how it would look at the various different screen sizes.

Please let us know if you have any questions or require any more info from us to get started. We are looking forward to seeing your designs!

-Pellham Journeys Marketing Team

```html
<!DOCTYPE html>
<html lang="en">
<head>
<meta charset="utf-8">
<title>Pellham Journeys – Travel Protection Options</title>
<link href="https://fonts.googleapis.com/css2?family=Rubik:wght@300;400;500;700&display=swap" rel="stylesheet">
<style>
:root{
  --red:#d42a35;
  --dark:#444444;
  --black:#222222;
  --ink:#1e1e1e;
  --text:#333333;
  --muted:#9a9a9a;
  --light:#f2f2f2;
  --white:#ffffff;
  --blue:#1d4fb8;
  --grey-tab:#bdbdbd;
  --grey-tab2:#a8a8a8;
}
*{box-sizing:border-box;margin:0;padding:0}
html,body{width:1200px;height:3514px;overflow:hidden}
body{font-family:"Rubik",sans-serif;color:var(--text);background:var(--white)}
.page{position:relative;width:1200px;height:3514px;overflow:hidden}
.abs{position:absolute}

/* header / hero */
.hero{left:0;top:0;width:1200px;height:832px;background:linear-gradient(180deg,#e4e4e4 0%,#cfcac3 45%,#8d7f70 75%,#6f655a 100%)}
.hero-photo{left:0;top:0;width:1200px;height:832px;background:radial-gradient(ellipse at 70% 55%,#b79b82 0%,rgba(160,130,110,.4) 35%,rgba(0,0,0,0) 65%)}
.brand{left:86px;top:36px;display:flex;align-items:center;gap:14px;white-space:nowrap}
.brand-mark{width:62px;height:62px;border-radius:50%;background:var(--red);flex:0 0 auto}
.brand-name{font-size:32px;font-weight:400;color:var(--blue)}
.step{left:780px;top:62px;font-size:17px;font-weight:500;color:var(--ink)}
.hero-title{left:130px;top:380px;font-size:57px;line-height:70px;font-weight:700;color:var(--ink)}
.hero-cut{left:0;top:732px}

/* intro */
.intro{left:0;top:832px;width:1200px;height:504px;background:var(--light);text-align:center}
.intro-lead{width:740px;margin:46px auto 0;font-size:27px;line-height:32px;font-weight:300;color:var(--ink)}
.intro-body{width:780px;margin:18px auto 0;font-size:17px;line-height:24px;font-weight:300;color:var(--ink)}
.btn-more{display:inline-flex;align-items:center;gap:18px;height:44px;padding:0 4px 0 24px;border:2px solid var(--red);border-radius:24px;font-size:17px;font-weight:400;color:var(--ink);text-decoration:none;background:var(--white)}
.btn-more .dot{width:36px;height:36px;border-radius:50%;background:var(--red);display:flex;align-items:center;justify-content:center}
.intro .btn-more{position:absolute;left:514px;top:289px}
.dark-cut{left:0;top:1220px}

/* plans */
.plans{left:0;top:1336px;width:1200px;height:750px;background:var(--dark)}
.plans-title{position:absolute;left:0;top:18px;width:1200px;text-align:center;font-size:34px;line-height:42px;font-weight:700;color:var(--white)}
.plan{position:absolute;top:138px;width:299px;height:513px;background:var(--white)}
.plan-head{height:128px;background:var(--black);color:var(--white);text-align:center;font-size:21px;font-weight:400;padding-top:38px;line-height:22px;position:relative;overflow:hidden}
.plan.featured .plan-head{background:var(--red)}
.plan-head .title{position:relative;z-index:1}
.price{position:absolute;left:107px;top:86px;width:84px;height:84px;border-radius:50%;background:var(--white);box-shadow:0 3px 8px rgba(0,0,0,.18);display:flex;align-items:center;justify-content:center;font-size:29px;font-weight:500;color:var(--ink)}
.price sup{font-size:15px;margin-right:2px;position:relative;top:-6px}
.plan.featured .price{color:var(--red)}
.plan-lead{margin:66px 14px 0;text-align:center;font-size:14.5px;line-height:20px;font-weight:500;color:var(--ink);letter-spacing:-.1px}
.plan-list{list-style:none;margin:26px 22px 0;font-size:12px;line-height:17px;font-weight:300;color:var(--text)}
.plan-list li{display:flex;gap:8px;margin-bottom:10px}
.plan-list li svg{flex:0 0 18px}
.plan-list li.neg{color:var(--red)}
.plan-list li.pos{color:var(--blue)}
.plan-list li.indent{padding-left:24px}
.plan-note{text-align:center;margin-top:82px;font-size:14px;font-weight:300;color:var(--ink)}
.btn-select{position:absolute;left:76px;bottom:-22px;width:146px;height:44px;border-radius:22px;background:var(--black);color:var(--white);font-size:17px;font-weight:500;display:flex;align-items:center;justify-content:center}
.plan.featured .btn-select{background:var(--red)}
.ribbon{position:absolute;left:-46px;top:12px;width:150px;height:18px;background:var(--white);transform:rotate(-30deg);color:var(--blue);font-size:10px;line-height:18px;text-align:center}

/* table */
.benefits{left:0;top:2086px;width:1200px;height:795px;background:var(--light)}
.bt-label{position:absolute;left:214px;top:92px;font-size:34px;font-weight:700;color:var(--ink)}
.bt-tab{position:absolute;top:68px;height:89px;display:flex;align-items:center;justify-content:center;text-align:center;font-size:21px;line-height:24px;color:var(--white)}
.tab-none{left:469px;width:198px;background:var(--grey-tab);border-radius:8px 0 0 0}
.tab-deluxe{left:667px;width:203px;background:var(--grey-tab2)}
.tab-cfar{left:870px;width:198px;background:var(--red);border-radius:0 8px 0 0}
.bt{position:absolute;left:132px;top:157px;width:936px;background:var(--white);border-radius:0 0 10px 10px;padding:10px 0 14px}
.row{display:grid;grid-template-columns:337px 198px 203px 198px;align-items:center;font-size:14px;font-weight:300;color:var(--ink);min-height:43px}
.row:nth-child(even){background:#f6f6f6}
.row>div{text-align:center;line-height:18px}
.row>div:first-child{padding-left:34px;line-height:19px;text-align:left}
.row.tall{min-height:62px}
.row.first{min-height:58px}

/* notes */
.notes{left:0;top:2881px;width:1200px;height:430px;background:var(--white)}
.note-frame{position:absolute;left:120px;top:105px;width:357px;height:257px;border:3px solid var(--red);border-radius:0 0 0 16px}
.note-photo{position:absolute;left:132px;top:78px;width:362px;height:270px;border-radius:10px;background:linear-gradient(135deg,#c9b48a 0%,#8d8a5c 40%,#4f5d47 75%,#2e3b35 100%)}
.note-list{position:absolute;left:540px;top:86px;width:524px;list-style:none;font-size:14px;line-height:22px;font-weight:300;color:var(--ink)}
.note-list li{display:flex;gap:10px;margin-bottom:14px}
.note-list li svg{flex:0 0 18px;margin-top:2px}
.notes .btn-more{position:absolute;left:570px;top:293px}

/* footer */
.footer{left:0;top:3311px;width:1200px;height:203px;background:var(--black)}
.footer .brand{left:340px;top:36px;gap:12px}
.footer .brand-mark{width:46px;height:46px}
.footer .brand-name{font-size:22px}
.social{position:absolute;left:625px;top:54px;display:flex;gap:8px}
.social span{width:33px;height:33px;border:1.5px solid #cfcfcf;border-radius:50%}
.footer-rule{position:absolute;left:24px;top:135px;width:1152px;height:1px;background:#555}
.copy{position:absolute;left:0;top:158px;width:1200px;text-align:center;font-size:15px;font-weight:300;color:#d8d8d8}
</style>
</head>
<body>
<div class="page">

  <header class="hero abs">
    <div class="hero-photo abs" role="img" aria-label="Four smiling students taking a selfie by a river with a gothic clock tower and parliament building behind them"></div>
    <div class="brand abs"><span class="brand-mark"></span><span class="brand-name">Pellham Journeys</span></div>
    <div class="step abs">STEP 7/8: TRAVEL PROTECTION OPTIONS</div>
    <h1 class="hero-title abs">PROTECT YOUR<br>TRIP INVESTMENT!</h1>
    <svg class="hero-cut abs" width="1200" height="100" viewBox="0 0 1200 100">
      <path d="M0 100 L689 13 L1200 80 L1200 100 Z" fill="#222"/>
      <path d="M0 100 L689 30 L1200 100 Z" fill="#f2f2f2"/>
    </svg>
  </header>

  <section class="intro abs">
    <p class="intro-lead">Harbourline Travel Assurance, a leading provider of group travel insurance, offers participants the opportunity to protect their travel investment.</p>
    <p class="intro-body">This program offers an array of travel protection benefits including 24/7 Worldwide Non-Insurance Assistance Services as well as Trip Cancellation, Trip Interruption, Medical Expense, Baggage and Personal Effects, and more travel insurance coverages such as the Cancel for Any Reason (CFAR) option, if eligible</p>
    <a class="btn-more" href="#">LEARN MORE <span class="dot"><svg width="18" height="14" viewBox="0 0 18 14"><path d="M1 2h16M1 7h12M1 12h8" stroke="#fff" stroke-width="2" stroke-linecap="round"/></svg></span></a>
  </section>

  <svg class="dark-cut abs" width="1200" height="117" viewBox="0 0 1200 117">
    <path d="M0 117 L689 7 L1200 117 Z" fill="#222"/>
    <path d="M0 117 L689 24 L1200 117 Z" fill="#444"/>
  </svg>

  <section class="plans abs">
    <h2 class="plans-title">TO START, PLEASE ENTER YOUR<br>TOTAL TRIP COST: $__</h2>

    <article class="plan" style="left:132px">
      <div class="plan-head"><span class="title">None</span></div>
      <div class="price"><sup>$</sup>0</div>
      <p class="plan-lead">Potentially lose 100% of your<br>tour cost</p>
      <p class="plan-note">- No Payment Protection</p>
      <a class="btn-select">SELECT</a>
    </article>

    <article class="plan" style="left:450px">
      <div class="plan-head"><span class="title">Student Deluxe</span></div>
      <div class="price"><sup>$</sup>100</div>
      <p class="plan-lead">Potentially lose 100% of your<br>tour cost</p>
      <ul class="plan-list">
        <li><svg width="18" height="18" viewBox="0 0 18 18"><circle cx="9" cy="9" r="7.5" fill="none" stroke="#555" stroke-width="1.2"/><path d="M5.5 9.3l2.4 2.3 4.8-5" fill="none" stroke="#555" stroke-width="1.3"/></svg><span>Trip Cancellation coverage provides a 100% refund if you need to cancel for covered reasons.</span></li>
        <li><svg width="18" height="18" viewBox="0 0 18 18"><circle cx="9" cy="9" r="7.5" fill="none" stroke="#555" stroke-width="1.2"/><path d="M5.5 9.3l2.4 2.3 4.8-5" fill="none" stroke="#555" stroke-width="1.3"/></svg><span>Includes additional coverages as per below Schedule.</span></li>
        <li class="neg"><svg width="18" height="18" viewBox="0 0 18 18"><circle cx="9" cy="9" r="7.5" fill="none" stroke="#d42a35" stroke-width="1.2"/><path d="M6 6l6 6M12 6l-6 6" stroke="#d42a35" stroke-width="1.3"/></svg><span>Does NOT include Cancel for Any Reason (CFAR)***.</span></li>
        <li class="neg indent"><svg width="18" height="18" viewBox="0 0 18 18"><circle cx="9" cy="9" r="7.5" fill="none" stroke="#d42a35" stroke-width="1.2"/><path d="M6 6l6 6M12 6l-6 6" stroke="#d42a35" stroke-width="1.3"/></svg><span>No coverage for cancellations due to fear of apandemic.</span></li>
      </ul>
      <a class="btn-select">SELECT</a>
    </article>

    <article class="plan featured" style="left:769px">
      <div class="plan-head"><span class="ribbon">Recommended</span><span class="title">Student Deluxe with<br>CFAR</span></div>
      <div class="price"><sup>$</sup>150</div>
      <p class="plan-lead">Protects your trip investment if you need to cancel for any reason***</p>
      <ul class="plan-list">
        <li><svg width="18" height="18" viewBox="0 0 18 18"><circle cx="9" cy="9" r="7.5" fill="none" stroke="#555" stroke-width="1.2"/><path d="M5.5 9.3l2.4 2.3 4.8-5" fill="none" stroke="#555" stroke-width="1.3"/></svg><span>Trip Cancellation coverage provides a 100% refund if you need to cancel for covered reasons.</span></li>
        <li><svg width="18" height="18" viewBox="0 0 18 18"><circle cx="9" cy="9" r="7.5" fill="none" stroke="#555" stroke-width="1.2"/><path d="M5.5 9.3l2.4 2.3 4.8-5" fill="none" stroke="#555" stroke-width="1.3"/></svg><span>Includes additional coverages as per below Schedule.</span></li>
        <li class="pos"><svg width="18" height="18" viewBox="0 0 18 18"><circle cx="9" cy="9" r="7.5" fill="none" stroke="#1d4fb8" stroke-width="1.2"/><path d="M5.5 9.3l2.4 2.3 4.8-5" fill="none" stroke="#1d4fb8" stroke-width="1.3"/></svg><span>Includes Cancel for Any Reason (CFAR)***</span></li>
        <li class="pos indent"><svg width="18" height="18" viewBox="0 0 18 18"><circle cx="9" cy="9" r="7.5" fill="none" stroke="#1d4fb8" stroke-width="1.2"/><path d="M5.5 9.3l2.4 2.3 4.8-5" fill="none" stroke="#1d4fb8" stroke-width="1.3"/></svg><span>Covers cancellation due to fear of a pandemic ***</span></li>
      </ul>
      <a class="btn-select">SELECT</a>
    </article>
  </section>

  <section class="benefits abs">
    <h2 class="bt-label">BENEFIT</h2>
    <div class="bt-tab tab-none">None</div>
    <div class="bt-tab tab-deluxe">Student<br>Deluxe</div>
    <div class="bt-tab tab-cfar">Student Deluxe<br>with CFAR</div>
    <div class="bt">
      <div class="row first"><div>CANCEL FOR ANY REASON (CFAR)***</div><div><svg width="16" height="16" viewBox="0 0 16 16"><circle cx="8" cy="8" r="7" fill="none" stroke="#aaa"/><path d="M5.5 5.5l5 5M10.5 5.5l-5 5" stroke="#aaa"/></svg></div><div><svg width="16" height="16" viewBox="0 0 16 16"><circle cx="8" cy="8" r="7" fill="none" stroke="#aaa"/><path d="M5.5 5.5l5 5M10.5 5.5l-5 5" stroke="#aaa"/></svg></div><div>CANCEL FOR ANY<br>REASON (CFAR)***:</div></div>
      <div class="row"><div>Trip Cancellation**</div><div><svg width="16" height="16" viewBox="0 0 16 16"><circle cx="8" cy="8" r="7" fill="none" stroke="#aaa"/><path d="M5.5 5.5l5 5M10.5 5.5l-5 5" stroke="#aaa"/></svg></div><div>Trip Cost*</div><div>Trip Cost*</div></div>
      <div class="row"><div>Trip Interruption**</div><div><svg width="16" height="16" viewBox="0 0 16 16"><circle cx="8" cy="8" r="7" fill="none" stroke="#aaa"/><path d="M5.5 5.5l5 5M10.5 5.5l-5 5" stroke="#aaa"/></svg></div><div>150% Trip Cost</div><div>150% of Trip Cost</div></div>
      <div class="row"><div>Travel Delay - 6 Hours</div><div><svg width="16" height="16" viewBox="0 0 16 16"><circle cx="8" cy="8" r="7" fill="none" stroke="#aaa"/><path d="M5.5 5.5l5 5M10.5 5.5l-5 5" stroke="#aaa"/></svg></div><div>$750 ($150/day)</div><div>$750 ($150/day)</div></div>
      <div class="row"><div>Missed Connection -3 Hours</div><div><svg width="16" height="16" viewBox="0 0 16 16"><circle cx="8" cy="8" r="7" fill="none" stroke="#aaa"/><path d="M5.5 5.5l5 5M10.5 5.5l-5 5" stroke="#aaa"/></svg></div><div>$500</div><div>$500</div></div>
      <div class="row"><div>Baggage/Personal Effects</div><div><svg width="16" height="16" viewBox="0 0 16 16"><circle cx="8" cy="8" r="7" fill="none" stroke="#aaa"/><path d="M5.5 5.5l5 5M10.5 5.5l-5 5" stroke="#aaa"/></svg></div><div>$1,500</div><div>$1,500</div></div>
      <div class="row"><div>Baggage Delay - 24 Hours</div><div><svg width="16" height="16" viewBox="0 0 16 16"><circle cx="8" cy="8" r="7" fill="none" stroke="#aaa"/><path d="M5.5 5.5l5 5M10.5 5.5l-5 5" stroke="#aaa"/></svg></div><div>$300</div><div>$300</div></div>
      <div class="row tall"><div>Emergency Medical Evacuation, Medical<br>Repatriation &amp; Return of Remains</div><div><svg width="16" height="16" viewBox="0 0 16 16"><circle cx="8" cy="8" r="7" fill="none" stroke="#aaa"/><path d="M5.5 5.5l5 5M10.5 5.5l-5 5" stroke="#aaa"/></svg></div><div>$100,000</div><div>$100,000</div></div>
      <div class="row"><div>Accident &amp; Sickness Medical Expense</div><div><svg width="16" height="16" viewBox="0 0 16 16"><circle cx="8" cy="8" r="7" fill="none" stroke="#aaa"/><path d="M5.5 5.5l5 5M10.5 5.5l-5 5" stroke="#aaa"/></svg></div><div>$25,000</div><div>$25,000</div></div>
      <div class="row"><div>Non-Medical Emergency Evacuation</div><div><svg width="16" height="16" viewBox="0 0 16 16"><circle cx="8" cy="8" r="7" fill="none" stroke="#aaa"/><path d="M5.5 5.5l5 5M10.5 5.5l-5 5" stroke="#aaa"/></svg></div><div>$100,000</div><div>$100,00</div></div>
      <div class="row tall"><div>Non-Insurance Worldwide Emergency<br>Assistance Services</div><div><svg width="16" height="16" viewBox="0 0 16 16"><circle cx="8" cy="8" r="7" fill="none" stroke="#aaa"/><path d="M5.5 5.5l5 5M10.5 5.5l-5 5" stroke="#aaa"/></svg></div><div>Included</div><div>Included</div></div>
    </div>
  </section>

  <section class="notes abs">
    <div class="note-frame"></div>
    <div class="note-photo" role="img" aria-label="Group of students gathered around a picnic table in a sunny park looking at a map"></div>
    <ul class="note-list">
      <li><svg width="18" height="18" viewBox="0 0 18 18"><circle cx="9" cy="9" r="7.5" fill="none" stroke="#555" stroke-width="1.2"/><path d="M5.5 9.3l2.4 2.3 4.8-5" fill="none" stroke="#555" stroke-width="1.3"/></svg><span>Coverages may vary and not all coverage is available in all jurisdictions. Totals listed below each coverage are the maximum benefit amount payable.</span></li>
      <li><svg width="18" height="18" viewBox="0 0 18 18"><circle cx="9" cy="9" r="7.5" fill="none" stroke="#555" stroke-width="1.2"/><path d="M5.5 9.3l2.4 2.3 4.8-5" fill="none" stroke="#555" stroke-width="1.3"/></svg><span>* Up to the lesser of the Trip Cost paid or the limit of Coverage for which benefits are requested and the appropriate plan cost has been paid. Maximum limit of $10,000</span></li>
      <li><svg width="18" height="18" viewBox="0 0 18 18"><circle cx="9" cy="9" r="7.5" fill="none" stroke="#555" stroke-width="1.2"/><path d="M5.5 9.3l2.4 2.3 4.8-5" fill="none" stroke="#555" stroke-width="1.3"/></svg><span>** For $0 Trip Cost, there is no Trip Cancellation and Trip Interruption is limited to $500 return air only</span></li>
    </ul>
    <a class="btn-more" href="#">LEARN MORE <span class="dot"><svg width="18" height="14" viewBox="0 0 18 14"><path d="M1 2h16M1 7h12M1 12h8" stroke="#fff" stroke-width="2" stroke-linecap="round"/></svg></span></a>
  </section>

  <footer class="footer abs">
    <div class="brand abs"><span class="brand-mark"></span><span class="brand-name">Pellham Journeys</span></div>
    <div class="social"><span></span><span></span><span></span><span></span></div>
    <div class="footer-rule"></div>
    <p class="copy">© 2020 Pellham Journeys. All Rights are Reserved.</p>
  </footer>

</div>
</body>
</html>
```